Disaster Recovery firm needs design for impactful Door Hanger flyer

We need the design for a 4.25X11 inch door hanger with die-cut included for the hanger. The hangers will be hung on the door medium to high net worth clientele's residential homes. They need to reference the event Hurricane Tova and speak to the issues that people have resulting from the storm and the benefits of our service. We will provide the sales language and bullet points.

Target Market(s)

Residential homeowners

Font styles to use
Sans Serif

Colors
3277b5
ec1f27
cee9f5
cedeed

Requirements
Must have
• Photos that include visual references to hurricane damage,
bullet points to convey the benefits of the service,
call to action, & company & local office contact information
Nice to have
• Great graphic design with layers & topics
Should not have
• Pictures of money, promises of "cash" or "no risk" and certain other violations of written statutes& compliance

```html
<!DOCTYPE html>
<html lang="en">
<head>
<meta charset="utf-8">
<title>Harborline Claims Consulting – Door Hanger</title>
<link href="https://fonts.googleapis.com/css2?family=Poppins:wght@500;700;800&family=Courier+Prime:wght@400;700&display=swap" rel="stylesheet">
<style>
  :root {
    --page-bg: #e6e7e9;
    --brand-blue: #1d5e86;
    --brand-blue-light: #3277b5;
    --brand-red: #d7262c;
    --ink: #231f20;
    --paper: #ffffff;
    --paper-tint: #eef1f4;
    --sky: #d9d6d4;
    --roof: #4f4352;
  }
  * { box-sizing: border-box; margin: 0; padding: 0; }
  html, body { width: 1200px; height: 800px; overflow: hidden; }
  body {
    background: var(--page-bg);
    font-family: "Poppins", sans-serif;
    color: var(--ink);
    position: relative;
  }
  .door-hanger {
    position: absolute;
    left: 450px;
    top: 18px;
    width: 300px;
    height: 764px;
    background: linear-gradient(160deg, var(--paper) 40%, var(--paper-tint) 100%);
    overflow: hidden;
  }
  .hero-art { position: absolute; left: 0; top: 0; width: 300px; height: 440px; }
  .hero-headline {
    position: absolute;
    left: 76px;
    top: 276px;
    color: var(--paper);
    font-weight: 800;
    font-size: 31px;
    line-height: 35px;
    letter-spacing: 0.5px;
    text-transform: uppercase;
    text-shadow: 0 2px 4px rgba(0,0,0,0.45);
  }
  .brand {
    position: absolute;
    left: 0; right: 0;
    top: 452px;
    text-align: center;
    color: var(--ink);
    font-weight: 500;
  }
  .brand-dot {
    display: block;
    width: 22px; height: 22px;
    margin: 0 auto 10px;
    border-radius: 50%;
    background: var(--brand-red);
  }
  .brand-name { font-size: 17px; letter-spacing: 3px; line-height: 20px; }
  .brand-sub { font-size: 10.5px; letter-spacing: 2px; line-height: 14px; }
  .pitch {
    position: absolute;
    left: 0; right: 0;
    top: 522px;
    text-align: center;
    font-weight: 700;
    font-size: 20.5px;
    line-height: 26px;
  }
  .services {
    position: absolute;
    top: 612px;
    left: 18px;
    right: 14px;
    display: grid;
    grid-template-columns: 1fr 1fr;
    column-gap: 10px;
    row-gap: 4px;
    list-style: none;
    font-family: "Courier Prime", monospace;
    font-size: 10.5px;
    line-height: 15px;
    text-transform: uppercase;
  }
  .services li { position: relative; padding-left: 11px; }
  .services li::before {
    content: "";
    position: absolute;
    left: 0; top: 4px;
    width: 7px; height: 7px;
    border-radius: 50%;
    background: var(--brand-red);
  }
  .services .col-right { grid-column: 2; }
  .call-label {
    position: absolute;
    left: 0; right: 0;
    top: 697px;
    text-align: center;
    color: var(--brand-red);
    font-weight: 800;
    font-size: 20px;
    line-height: 24px;
  }
  .phone-band {
    position: absolute;
    left: 0; right: 0;
    top: 724px;
    height: 38px;
    background: linear-gradient(90deg, #e3e7eb 0%, #e3e7eb 8%, var(--brand-blue) 20%, var(--brand-blue-light) 55%, var(--brand-blue) 100%);
    display: flex;
    align-items: center;
    padding-left: 32px;
    gap: 14px;
  }
  .phone-icon { width: 30px; height: 30px; flex: none; }
  .phone-number {
    color: var(--paper);
    font-weight: 700;
    font-size: 26px;
    letter-spacing: 0.5px;
  }
</style>
</head>
<body>
  <main class="door-hanger">
    <svg class="hero-art" viewBox="0 0 300 440" aria-hidden="false">
      <defs>
        <linearGradient id="bandBlue" x1="0" y1="0" x2="1" y2="1">
          <stop offset="0" stop-color="#1d5e86"/>
          <stop offset="0.6" stop-color="#2a6e9c"/>
          <stop offset="1" stop-color="#1b587f"/>
        </linearGradient>
        <linearGradient id="stormPhoto" x1="0" y1="0" x2="1" y2="1">
          <stop offset="0" stop-color="#cfcac7"/>
          <stop offset="0.35" stop-color="#6a5a66"/>
          <stop offset="0.6" stop-color="#4f4352"/>
          <stop offset="0.85" stop-color="#7c7070"/>
          <stop offset="1" stop-color="#b8b2ae"/>
        </linearGradient>
      </defs>
      <path class="blue-sweep" d="M0,0 H300 V372 C210,372 110,400 0,412 Z" fill="url(#bandBlue)"/>
      <path class="white-swoosh" d="M0,20 H300 V366 H128 C52,366 14,330 0,258 Z" fill="#ffffff"/>
      <g role="img" aria-label="Photo of a storm-damaged house roof under dark hurricane clouds">
        <path d="M0,20 H255 Q300,20 300,65 V356 H132 C62,356 22,322 0,240 Z" fill="url(#stormPhoto)"/>
      </g>
      <circle class="hanger-hole" cx="150" cy="88" r="45" fill="#e6e7e9"/>
    </svg>

    <h1 class="hero-headline">The Storm<br>Caught You</h1>

    <div class="brand">
      <span class="brand-dot"></span>
      <div class="brand-name">HARBORLINE CLAIMS</div>
      <div class="brand-sub">CONSULTING</div>
    </div>

    <h2 class="pitch">Make The Best Decision<br>For Your Roof<br>And Home</h2>

    <ul class="services">
      <li>Hail damage</li>
      <li>Roof repairs</li>
      <li>Wind damage</li>
      <li>Gutter repairs</li>
      <li>Storm damage</li>
      <li>Siding repairs</li>
      <li>Roof inspections</li>
      <li>Window repairs</li>
    </ul>

    <p class="call-label">CALL US TODAY</p>

    <div class="phone-band">
      <svg class="phone-icon" viewBox="0 0 30 30" aria-hidden="true">
        <circle cx="15" cy="15" r="13" fill="#ffffff" stroke="#d7262c" stroke-width="2"/>
        <path d="M10.5,8.5 L13,8 L14.3,11.4 L12.7,12.7 C13.6,14.7 15.3,16.4 17.3,17.3 L18.6,15.7 L22,17 L21.5,19.5 C21.3,20.4 20.5,21 19.6,21 C13.7,20.6 9.4,16.3 9,10.4 C9,9.5 9.6,8.7 10.5,8.5 Z" fill="#d7262c"/>
      </svg>
      <span class="phone-number">555.013.4720</span>
    </div>
  </main>
</body>
</html>
```